Halvorsen Partners Business Card

Halvorsen Partners Civil Construction
Marcus Halvorsen
CEO
727-518-6094
Marcus@HalvorsenSiteworks.example
www.HalvorsenSiteworks.example
Site Development
Utility Construction
Excavation
40876 County Lane 19
Land O' Lakes, FL 34638

Target Market(s)

Construction and government

Industry/Entity Type

Business

Contact Information for Business Card

I want an unique design that make a statement

Number of Pages Required

1 page

Font styles to use

Colors

Designer to choose colors to be used in the design.

Requirements
Must have
• unique design, feel free to modify or change the color of my logo.
Nice to have
• extra design features like spot UV, foil accents, color edges, unique paper, or any thing that would make my card pop.
• I like the feel of the image that I attached

```html
<!DOCTYPE html>
<html lang="en">
<head>
<meta charset="utf-8">
<title>Halvorsen Partners Business Card</title>
<link href="https://fonts.googleapis.com/css2?family=Source+Sans+3:wght@300;400;600&display=swap" rel="stylesheet">
<style>
  :root {
    --canvas: #d6d7da;
    --card-dark: #1f2022;
    --card-light: #f7f7f8;
    --brand-blue: #2f4fd6;
    --ink-grey: #6d6f74;
    --soft-grey: #8a8c90;
    --rule-grey: #4a4b4e;
    --light-rule: #e6e7ea;
  }
  * { margin: 0; padding: 0; box-sizing: border-box; }
  html, body { width: 1200px; height: 1200px; overflow: hidden; }
  body {
    background: var(--canvas);
    font-family: "Source Sans 3", "Helvetica Neue", Arial, sans-serif;
    display: flex;
    flex-direction: column;
    align-items: center;
    justify-content: center;
    gap: 60px;
  }
  .card {
    width: 900px;
    height: 514px;
    position: relative;
    box-shadow: 0 10px 30px rgba(0,0,0,0.18);
    overflow: hidden;
  }

  /* Front side */
  .card-front { background: var(--card-dark); }
  .brand-lockup {
    position: absolute;
    left: 90px;
    top: 150px;
    display: flex;
    align-items: center;
    gap: 34px;
  }
  .brand-square {
    width: 92px;
    height: 92px;
    background: var(--brand-blue);
  }
  .brand-divider {
    width: 2px;
    height: 120px;
    background: var(--rule-grey);
  }
  .brand-text { display: flex; flex-direction: column; gap: 6px; }
  .brand-name {
    color: var(--brand-blue);
    font-weight: 600;
    font-size: 54px;
    letter-spacing: 1px;
    text-transform: uppercase;
    line-height: 1;
  }
  .brand-tagline {
    color: var(--ink-grey);
    font-weight: 300;
    font-size: 26px;
    letter-spacing: 12px;
    text-transform: uppercase;
  }
  .services {
    position: absolute;
    left: 90px;
    bottom: 70px;
    display: flex;
    align-items: center;
    gap: 22px;
    color: var(--soft-grey);
    font-size: 22px;
    font-weight: 300;
  }
  .services .sep {
    width: 2px;
    height: 28px;
    background: var(--brand-blue);
  }

  /* Back side */
  .card-back {
    background: linear-gradient(135deg, #ffffff 0%, var(--card-light) 55%, #ececee 100%);
  }
  .holder {
    position: absolute;
    left: 80px;
    top: 70px;
  }
  .holder-name {
    color: var(--brand-blue);
    font-weight: 600;
    font-size: 64px;
    line-height: 1;
    letter-spacing: -0.5px;
  }
  .holder-title {
    color: var(--ink-grey);
    font-weight: 400;
    font-size: 40px;
    line-height: 1.1;
    margin-top: 4px;
  }
  .contact-list {
    position: absolute;
    left: 330px;
    top: 250px;
    list-style: none;
    display: flex;
    flex-direction: column;
    gap: 22px;
  }
  .contact-item {
    display: flex;
    align-items: center;
    gap: 20px;
    color: var(--ink-grey);
    font-size: 25px;
    font-weight: 400;
  }
  .contact-icon { width: 34px; height: 34px; flex: none; }
</style>
</head>
<body>

<section class="card card-front" aria-label="Business card front">
  <div class="brand-lockup">
    <div class="brand-square"></div>
    <div class="brand-divider"></div>
    <div class="brand-text">
      <span class="brand-name">Halvorsen Partners</span>
      <span class="brand-tagline">Civil Construction</span>
    </div>
  </div>
  <div class="services">
    <span>Site Development</span>
    <span class="sep"></span>
    <span>Utility Construction</span>
    <span class="sep"></span>
    <span>Excavation</span>
  </div>
</section>

<section class="card card-back" aria-label="Business card back">
  <div class="holder">
    <div class="holder-name">Marcus Halvorsen</div>
    <div class="holder-title">CEO</div>
  </div>
  <ul class="contact-list">
    <li class="contact-item">
      <svg class="contact-icon" viewBox="0 0 34 34" fill="none" stroke="#2f4fd6" stroke-width="2.4">
        <rect x="6" y="10" width="22" height="16" rx="3" transform="rotate(-12 17 18)"/>
      </svg>
      <span>727-518-6094</span>
    </li>
    <li class="contact-item">
      <svg class="contact-icon" viewBox="0 0 34 34" fill="none" stroke="#2f4fd6" stroke-width="2.2">
        <rect x="4" y="9" width="26" height="18" rx="1"/>
        <path d="M4 10 L17 20 L30 10"/>
      </svg>
      <span>Marcus@HalvorsenSiteworks.example</span>
    </li>
    <li class="contact-item">
      <svg class="contact-icon" viewBox="0 0 34 34" fill="none" stroke="#2f4fd6" stroke-width="2">
        <circle cx="17" cy="17" r="13" fill="#2f4fd6" fill-opacity="0.12"/>
        <ellipse cx="17" cy="17" rx="6" ry="13"/>
        <line x1="4" y1="17" x2="30" y2="17"/>
        <line x1="6" y1="10" x2="28" y2="10"/>
        <line x1="6" y1="24" x2="28" y2="24"/>
      </svg>
      <span>www.HalvorsenSiteworks.example</span>
    </li>
  </ul>
</section>

</body>
</html>
```